Nutrivana, site for appointments between nutritionists and patients

Nutrivana is a platform for connecting nutritionists and patients with appointment scheduling and online payment.

We like teal, but we're not fixated on it.

The site must be simple, accessible and pleasant and dynamic and evoke the joy of nutrition while not forgetting the health aspect.

Example of illustration which tend towards what we are looking for.

Logo and graphic charter

Home page, simple little information

1)
Book a physical or video consultation with a dietitian (medirendo, you stay calm, lorée, vantoc)

2)
Reason for using Nutrivana

Access state-certified nutrition experts with several years of training (registration of professionals on the site only with adeli number and valid diploma)

Access the availability of tens of thousands of healthcare professionals.

Make an appointment online, 24/7, for a physical or video consultation.

Secure personal data

3)
You are a dietitian nutritionist

Use nutrivana to optimize your activity
Free up time by making an appointment online
Limit unfulfilled appointments with online payment
Take advantage of Nutrivana's notoriety to obtain better visibility
Use a commercial platform to develop your patient base
Use the platform's communication tools
Etc ...

Page 2 if applicable

List of professionals

Page 3 if search by specific name

Name photo
The essentials, map and access information, presentation, timetables, prices, site, make an appointment

Page 3 bis more in-depth presentation.

Page 4
agenda appointment booking page

Payment page

Professional page

Page 1
presentation of assets

Page 2 limited access

Rates with bronze, silver, gold, platinum account

Products, training and services page for sale

Blog page

Nutrivana is a platform that connects nutritionists and patients with online appointments and payment.

We like the teal color but we are not set on it.

The site must be simple, accessible, pleasant and dynamic and evoke the joy of nutrition while not forgetting the health aspect.

Example of illustrations that tend towards what we are looking for.

Our Logo is on the attachment

Home page

1)
Book a physical or video consultation with a dietician (ex site: medirendo, you stay calm, lorée, vantoc)

2)
Reasons to use Nutrivana

Access to experts in nutrition with several years of training (registration of professionals on the site only with adeli number and valid diploma)

Access the availability of tens of thousands of dieticians.

Secure personal data

3) You are a dietitian nutritionist

Free up time with online appointment booking
Limit the number of missed appointments thanks to online payment
Take advantage of Nutrivana's notoriety to get a better visibility
Use the communication tools of the platform
Etc ...

Page 2 if the patient don't choose a professional and put only a place.

List of professionals

Page 3 if searching by specific name

Photo name
The essentials, map and access information, presentation, opening hours, rates, site, make an appointment

Page 3 bis - more detailed presentation of dietician.

Page 4
diary page for making an appointment

Payment page

Blog page

Side Professional page

Page 1
presentation of assets

Page 2 (limited access)

Page 3

Products, training and services for sale page

Pour laisser le temps aux designers de travailler.

Target Market(s)

The general public

Number of Pages Required

5+ page

Colors
00AB8E
00BBA5
67D7C9
C6EFE9
E9F9F6

Requirements
Must have
• Read the project in the attached documents. Read the project on the attachments
Should not have
• No photographs

```html
<!DOCTYPE html>
<html lang="en">
<head>
<meta charset="utf-8">
<title>Nutrivana – Book a consultation with a dietician</title>
<link href="https://fonts.googleapis.com/css2?family=Quicksand:wght@500;600;700&family=Roboto:wght@400;500;700&display=swap" rel="stylesheet">
<style>
:root{
  --teal:#00ab8e;
  --teal-deep:#179f7e;
  --teal-dark:#0f5a47;
  --teal-mid:#00bba5;
  --teal-soft:#67d7c9;
  --teal-pale:#c6efe9;
  --teal-mist:#e9f9f6;
  --ink:#111;
  --text:#444;
  --orange:#f0572a;
  --white:#fff;
}
*{box-sizing:border-box;margin:0;padding:0}
html,body{width:1200px;height:2586px;overflow:hidden;background:var(--white)}
body{position:relative;font-family:"Roboto",sans-serif;color:var(--text)}
.abs{position:absolute}
.heading{font-family:"Quicksand",sans-serif;font-weight:700;color:var(--ink)}
.accent{color:var(--teal);font-weight:600}

/* hero */
.hero{left:0;top:0;width:1200px;height:700px;overflow:hidden}
.hero-bg{left:0;top:0}
.brand{display:flex;align-items:center;gap:7px;font-family:"Quicksand",sans-serif;font-weight:700;color:var(--orange);white-space:nowrap}
.brand-dot{border-radius:50%;background:var(--orange);flex:none}
.site-brand{left:110px;top:92px;font-size:22px}
.site-brand .brand-dot{width:10px;height:10px}
.nav{left:279px;top:54px;display:flex;gap:27px;font-size:15px;font-weight:500;color:#1a1a1a}
.nav-cta{left:916px;top:45px;width:170px;height:44px;border-radius:22px;background:var(--teal-deep);color:#fff;font-size:15px;font-weight:500;display:flex;align-items:center;justify-content:center}
.hero-title{left:110px;top:200px;font-size:41px;line-height:51px;width:560px}
.search{left:111px;top:396px;width:540px;height:52px;display:flex;background:#fff;box-shadow:0 2px 8px rgba(0,0,0,.06)}
.search-field{display:flex;align-items:center;gap:6px;padding-left:16px;font-size:10px;color:#444}
.search-field.name{width:222px;border-right:1px solid #ddd}
.search-field.place{width:172px;padding-left:22px}
.search-btn{flex:1;background:var(--teal-deep);color:#fff;font-weight:700;font-size:15px;display:flex;align-items:center;justify-content:center}
.hero-art{left:700px;top:140px;width:395px;height:515px;background:radial-gradient(ellipse 50% 50% at 55% 50%,rgba(23,159,126,.85),rgba(47,169,135,.55) 45%,rgba(166,228,217,0) 100%)}

/* reasons */
.reasons-title{left:0;top:765px;width:1200px;text-align:center;font-size:41px}
.card{top:858px;width:228px;height:254px;background:#fff;border-radius:4px;box-shadow:0 6px 18px rgba(0,0,0,.13);display:flex;flex-direction:column;align-items:center;padding:42px 24px 0;text-align:center}
.card-icon{width:80px;height:80px}
.card-text{margin-top:16px;font-size:17px;font-weight:500;line-height:26px;color:#111}

/* pro section */
.pro{left:0;top:1235px;width:1200px;height:605px;background:var(--teal-mist)}
.pro-art{left:118px;top:1252px;width:460px;height:508px;background:radial-gradient(ellipse 48% 50% at 45% 50%,rgba(60,207,176,.9),rgba(126,240,215,.6) 50%,rgba(233,249,246,0) 100%)}
.pro-title{left:600px;top:1300px;font-size:48px;line-height:56px}
.checklist{left:600px;top:1436px;list-style:none;font-size:15px;color:#555}
.checklist li{display:flex;align-items:center;gap:17px;height:31.8px}
.btn{display:flex;align-items:center;justify-content:center;gap:10px;font-weight:700;font-size:17px;border-radius:24px}
.learn{left:601px;top:1666px;width:188px;height:48px;background:var(--teal-deep);color:#fff}

/* cta */
.cta{left:0;top:1840px;width:1200px;height:410px}
.cta-title{left:0;top:1886px;width:1200px;text-align:center;color:#fff;font-size:40px;line-height:43px}
.cta-text{left:150px;top:2004px;width:900px;text-align:center;color:#fff;font-size:15px;line-height:26px}
.book{left:501px;top:2074px;width:200px;height:48px;background:#fff;color:var(--teal-deep)}

/* footer */
.footer-brand{left:115px;top:2448px;font-size:40px}
.footer-brand .brand-dot{width:16px;height:16px}
.foot-col{top:2305px}
.foot-col h3{font-size:18px;font-weight:500;color:#333;margin-bottom:18px}
.foot-col li{list-style:none;font-size:14px;color:#555;height:27.6px}
.contact{display:flex;gap:12px;margin-bottom:12px;font-size:14px;color:#555;line-height:20px}
.contact b{display:block;font-size:12px;color:#222}
.footer-rule{left:111px;top:2521px;width:978px;height:1px;background:#ccc}
.socials{left:111px;top:2542px;display:flex;gap:8px}
.social{width:29px;height:29px;border:1.5px solid #333;border-radius:50%}
.copyright{left:0;top:2549px;width:1200px;text-align:center;font-size:15px;color:#444}
.to-top{left:1107px;top:2506px;width:36px;height:36px;border-radius:50%;background:var(--teal-deep);display:flex;align-items:center;justify-content:center}
</style>
</head>
<body>

<section class="hero abs">
  <svg class="hero-bg abs" width="1200" height="700" viewBox="0 0 1200 700" aria-hidden="true">
    <defs>
      <pattern id="stripes" width="8" height="8" patternUnits="userSpaceOnUse" patternTransform="rotate(45)">
        <rect width="8" height="8" fill="#b9ebe2"/>
        <rect width="3" height="8" fill="#b2e7de"/>
      </pattern>
    </defs>
    <path d="M0 0H1200V578C1080 650 880 700 620 690C360 680 200 610 0 625Z" fill="url(#stripes)"/>
    <path d="M0 540C120 535 260 590 420 640C240 620 110 615 0 625Z" fill="#5ad0bb"/>
  </svg>

  <div class="brand site-brand abs"><span class="brand-dot"></span>nutrivana</div>
  <nav class="nav abs"><span>Home</span><span>List Of Professionals</span><span>Presentation Of Dietician</span><span>Making An Appointment</span></nav>
  <div class="nav-cta abs">Book a physical</div>

  <h1 class="hero-title heading abs">Book a Physical or Video Consultation <span class="accent">With a Healthcare Professional</span></h1>

  <div class="search abs">
    <div class="search-field name">
      <svg width="10" height="10" viewBox="0 0 10 10" aria-hidden="true"><circle cx="4" cy="4" r="3" fill="none" stroke="#333" stroke-width="1.5"/><path d="M6.2 6.2L9 9" stroke="#333" stroke-width="1.5"/></svg>
      Name, specialty, establishment, ...
    </div>
    <div class="search-field place">
      <svg width="8" height="10" viewBox="0 0 8 10" aria-hidden="true"><path d="M4 10C1 6 0 5 0 4a4 4 0 018 0c0 1-1 2-4 6z" fill="#333"/><circle cx="4" cy="4" r="1.4" fill="#fff"/></svg>
      Where ?
    </div>
    <div class="search-btn">TO RESEARCH</div>
  </div>

  <div class="hero-art abs" role="img" aria-label="Isometric illustration of a patient shaking hands with a doctor stepping out of a smartphone, surrounded by medical record panels"></div>
</section>

<h2 class="reasons-title heading abs">Reasons to <span class="accent">use Nutrivana</span></h2>

<div class="card abs" style="left:98px">
  <svg class="card-icon" viewBox="0 0 80 80" role="img" aria-label="Checklist clipboard icon">
    <rect x="2" y="6" width="52" height="68" rx="3" fill="none" stroke="#179f7e" stroke-width="3"/>
    <rect x="18" y="2" width="20" height="9" rx="2" fill="#179f7e"/>
    <g fill="none" stroke="#179f7e" stroke-width="2.5"><rect x="10" y="20" width="8" height="8"/><rect x="10" y="36" width="8" height="8"/><rect x="10" y="52" width="8" height="8"/><path d="M24 24h22M24 40h22M24 56h14"/></g>
    <circle cx="62" cy="60" r="15" fill="#179f7e"/>
    <path d="M62 45c0-5 3-8 7-9" fill="none" stroke="#179f7e" stroke-width="2.5"/>
  </svg>
  <p class="card-text">Access to experts in nutrition with several years of training</p>
</div>
<div class="card abs" style="left:355px">
  <svg class="card-icon" viewBox="0 0 80 80" role="img" aria-label="Produce basket and health plus icon">
    <circle cx="52" cy="20" r="11" fill="none" stroke="#179f7e" stroke-width="3"/>
    <path d="M36 62c0-14 7-24 16-24s16 10 16 24z" fill="none" stroke="#179f7e" stroke-width="3"/>
    <path d="M6 42h38l-5 24H11z" fill="#179f7e"/>
    <path d="M12 36c-4-6-2-12 4-14 2 6 0 10-4 14zM24 36c4-6 10-8 14-6-2 6-8 8-14 6z" fill="none" stroke="#179f7e" stroke-width="2.5"/>
    <rect x="54" y="48" width="14" height="14" rx="2" fill="#179f7e"/>
    <path d="M61 51v8M57 55h8" stroke="#fff" stroke-width="2"/>
  </svg>
  <p class="card-text">Access the availability of tens of thousands of dieticians.</p>
</div>
<div class="card abs" style="left:612px">
  <svg class="card-icon" viewBox="0 0 80 80" role="img" aria-label="Round 24/7 clock icon">
    <circle cx="40" cy="40" r="34" fill="none" stroke="#179f7e" stroke-width="2" stroke-dasharray="2 3"/>
    <path d="M58 12a34 34 0 0116 28" fill="none" stroke="#179f7e" stroke-width="3"/>
    <path d="M56 6l4 7-8 1z" fill="#179f7e"/>
    <circle cx="40" cy="40" r="25" fill="#179f7e"/>
    <text x="40" y="46" text-anchor="middle" font-family="Quicksand,sans-serif" font-weight="700" font-size="17" fill="#fff">24/7</text>
  </svg>
  <p class="card-text">Make an appointment online, 24/7, for a physical or video consultation.</p>
</div>
<div class="card abs" style="left:869px">
  <svg class="card-icon" viewBox="0 0 80 80" role="img" aria-label="Laptop with secure user profile icon">
    <rect x="10" y="14" width="60" height="40" rx="3" fill="none" stroke="#179f7e" stroke-width="3"/>
    <path d="M2 58h76l-4 6H6z" fill="#179f7e"/>
    <circle cx="40" cy="30" r="6" fill="none" stroke="#179f7e" stroke-width="2.5"/>
    <path d="M29 47c1-7 6-10 11-10s10 3 11 10" fill="none" stroke="#179f7e" stroke-width="2.5"/>
    <path d="M16 22h8M16 28h8M56 22h8M56 28h8M56 34h8" stroke="#179f7e" stroke-width="2.5"/>
  </svg>
  <p class="card-text">Secure personal data</p>
</div>

<section class="pro abs"></section>
<div class="pro-art abs" role="img" aria-label="Isometric illustration of a doctor on a smartphone video call with a patient holding a phone, with a stethoscope in front"></div>
<h2 class="pro-title heading abs">You are a dietitian<br><span class="accent">nutritionist</span></h2>
<ul class="checklist abs">
  <li><svg width="14" height="14" viewBox="0 0 14 14" aria-hidden="true"><circle cx="7" cy="7" r="7" fill="#179f7e"/><path d="M4 7.2l2 2 4-4" fill="none" stroke="#fff" stroke-width="1.7"/></svg>Use nutrivana to optimize your activity</li>
  <li><svg width="14" height="14" viewBox="0 0 14 14" aria-hidden="true"><circle cx="7" cy="7" r="7" fill="#179f7e"/><path d="M4 7.2l2 2 4-4" fill="none" stroke="#fff" stroke-width="1.7"/></svg>Free up time with online appointment booking</li>
  <li><svg width="14" height="14" viewBox="0 0 14 14" aria-hidden="true"><circle cx="7" cy="7" r="7" fill="#179f7e"/><path d="M4 7.2l2 2 4-4" fill="none" stroke="#fff" stroke-width="1.7"/></svg>Limit the number of missed appointments thanks to online payment</li>
  <li><svg width="14" height="14" viewBox="0 0 14 14" aria-hidden="true"><circle cx="7" cy="7" r="7" fill="#179f7e"/><path d="M4 7.2l2 2 4-4" fill="none" stroke="#fff" stroke-width="1.7"/></svg>Take advantage of Nutrivana's notoriety to get a better visibility</li>
  <li><svg width="14" height="14" viewBox="0 0 14 14" aria-hidden="true"><circle cx="7" cy="7" r="7" fill="#179f7e"/><path d="M4 7.2l2 2 4-4" fill="none" stroke="#fff" stroke-width="1.7"/></svg>Use a commercial platform to develop your patient base</li>
  <li><svg width="14" height="14" viewBox="0 0 14 14" aria-hidden="true"><circle cx="7" cy="7" r="7" fill="#179f7e"/><path d="M4 7.2l2 2 4-4" fill="none" stroke="#fff" stroke-width="1.7"/></svg>Use the communication tools of the platform</li>
</ul>
<div class="btn learn abs">LEARN MORE <svg width="16" height="16" viewBox="0 0 16 16" aria-hidden="true"><circle cx="8" cy="8" r="8" fill="#fff"/><path d="M6.5 4.5L10 8l-3.5 3.5" fill="none" stroke="#179f7e" stroke-width="2"/></svg></div>

<svg class="cta abs" width="1200" height="410" viewBox="0 0 1200 410" aria-hidden="true">
  <path d="M0 0H1200V230C1000 320 600 360 360 395C220 400 90 360 0 300Z" fill="#5ad4bd"/>
  <path d="M0 0H1200V225C900 300 620 355 400 392C220 405 90 350 0 300Z" fill="#179f7e"/>
</svg>
<h2 class="cta-title heading abs">Book a physical or video consultation<br>with a dietician</h2>
<p class="cta-text abs">Lorem ipsum dolor sit amet, consectetur adipiscing elit, sed do eiusmod tempor incididunt ut labore et dolore magna aliqua. Ut enim ad minim veniam, quis nostrud exercitation ullamco laboris nisi ut aliquip ex ea commodo consequat.</p>
<div class="btn book abs">BOOK NOW <svg width="16" height="16" viewBox="0 0 16 16" aria-hidden="true"><circle cx="8" cy="8" r="8" fill="#179f7e"/><path d="M6.5 4.5L10 8l-3.5 3.5" fill="none" stroke="#fff" stroke-width="2"/></svg></div>

<footer>
  <div class="brand footer-brand abs"><span class="brand-dot"></span>nutrivana</div>
  <div class="foot-col abs" style="left:396px">
    <h3>Quick Links</h3>
    <ul><li>Home</li><li>List Of Professionals</li><li>Presentation Of Dietician</li><li>Making An Appointment</li><li>Contact Us</li></ul>
  </div>
  <div class="foot-col abs" style="left:641px">
    <h3>About Company</h3>
    <ul><li>Privacy Policy</li><li>Terms of Service</li><li>Site Map</li><li>Imprint</li><li>Terms And Conditions</li></ul>
  </div>
  <div class="foot-col abs" style="left:855px">
    <h3>Contact Us</h3>
    <div class="contact"><svg width="12" height="12" viewBox="0 0 12 12" aria-hidden="true"><path d="M2.5 0.5l2 2.5-1.2 1.5c.7 1.6 1.9 2.8 3.5 3.5L8.3 6.8l2.7 2-1 2.4C5 11 1 7 .6 2z" fill="#179f7e"/></svg><div><b>Phone</b>(555) 014-2290</div></div>
    <div class="contact"><svg width="14" height="11" viewBox="0 0 14 11" aria-hidden="true"><rect width="14" height="11" rx="1" fill="#179f7e"/><path d="M1 1.5l6 4.5 6-4.5" fill="none" stroke="#fff" stroke-width="1.3"/></svg><div><b>Email</b>info@nutrivana.com</div></div>
    <div class="contact"><svg width="10" height="13" viewBox="0 0 8 10" aria-hidden="true"><path d="M4 10C1 6 0 5 0 4a4 4 0 018 0c0 1-1 2-4 6z" fill="#179f7e"/><circle cx="4" cy="4" r="1.4" fill="#fff"/></svg><div><b>Location</b>2425 Lorem ipsum dolor sit amet,<br>consectetur adipiscing elit,</div></div>
  </div>
  <div class="footer-rule abs"></div>
  <div class="socials abs"><span class="social"></span><span class="social"></span><span class="social"></span><span class="social"></span></div>
  <p class="copyright abs">2021 Copyright -&nbsp; Nutrivana &nbsp;| All Rights Reserved</p>
  <div class="to-top abs"><svg width="14" height="10" viewBox="0 0 14 10" aria-hidden="true"><path d="M2 8l5-5 5 5" fill="none" stroke="#fff" stroke-width="2.2"/></svg></div>
</footer>

</body>
</html>
```